Flyer Design

The company nane is "MARLO DUNE EARTHWORKS" it is a earthmoving company using a skid steer or korvex with tracks, the type of work I will be doing range from site cleans, pavings preps, house pads, final trim, landscaping, pool digs. Call 0491570156

i have posted a foto of the new design for the logo, please incorporate somehow, also i am using a velmor glide rig vk30 skid steer, i am not using a front end loader or digger or anu other earthmoving gear so dont use them.

Reason: more time for more ideas

include easy narrow access

Very experienced in all aspects of korvex work. Rubbish removal. House and shed pads. Paving prep Concrete removal. Lawn removal. Clearing Limestone driveways. Limestone block lifting. Levelling.

If you want it done fast. Wether your after site cleans, paving preps, earth moving, house pads, final trim or yard demos we cater for the lot. Our specialty equipment can do the lot

I have uploaded 2 new pictures, one is the actual logo of the business and the other is the picture I want used on the flyer, think outside the box

House

```html
<!DOCTYPE html>
<html lang="en">
<head>
<meta charset="utf-8">
<title>Marlo Dune Earthworks Flyer</title>
<link href="https://fonts.googleapis.com/css2?family=Black+Ops+One&family=Roboto+Condensed:ital,wght@0,700;1,700&family=Exo+2:ital,wght@1,500;1,600&display=swap" rel="stylesheet">
<style>
  :root {
    --orange: #e2692a;
    --orange-deep: #c9561c;
    --ink: #1f1c1a;
    --dark: #272421;
    --charcoal: #33312f;
    --white: #ffffff;
    --soil-1: #5a3f28;
    --soil-2: #7a5636;
  }
  * { margin: 0; padding: 0; box-sizing: border-box; }
  html, body { width: 892px; height: 1200px; overflow: hidden; background: var(--dark); }
  .flyer { position: relative; width: 892px; height: 1200px; background: var(--dark); overflow: hidden; font-family: "Roboto Condensed", "Arial Narrow", sans-serif; }

  .headline-bar { position: absolute; left: 0; top: 0; width: 892px; height: 84px; background: var(--orange); display: flex; align-items: center; justify-content: center; }
  .headline { font-family: "Black Ops One", "Impact", sans-serif; font-size: 41px; letter-spacing: 3px; color: var(--ink); text-transform: uppercase; }

  .hero-photo { position: absolute; left: 0; top: 84px; width: 892px; height: 430px;
    background: linear-gradient(180deg, #8d8a84 0%, #6f6b62 35%, #a48a66 62%, #7d5c3c 100%); }
  .hero-fade { position: absolute; left: 0; top: 300px; width: 892px; height: 420px; }

  .badge { position: absolute; left: 628px; top: 315px; width: 178px; height: 164px; }
  .badge-text { position: absolute; left: 628px; top: 347px; width: 178px; text-align: center; color: var(--white); font-weight: 700; line-height: 1.02; }
  .badge-text .small { font-size: 22px; display: block; }
  .badge-text .large { font-size: 29px; letter-spacing: 2px; display: block; margin-top: 2px; }

  .brand { position: absolute; left: 0; top: 522px; width: 892px; text-align: center; color: var(--white); font-weight: 700; text-transform: uppercase; }
  .brand-name { display: block; font-size: 116px; line-height: 1; letter-spacing: -1px; }
  .brand-sub { display: block; font-size: 50px; line-height: 1; letter-spacing: 6px; margin-top: 8px; }

  .soil-photo { position: absolute; left: 0; top: 740px; width: 892px; height: 350px;
    background: linear-gradient(180deg, rgba(39,36,33,1) 0%, rgba(74,52,33,0.9) 22%, var(--soil-1) 50%, var(--soil-2) 100%); }

  .services-head { position: absolute; left: 49px; top: 734px; display: flex; align-items: center; gap: 14px; }
  .services-icon { width: 52px; height: 52px; }
  .services-title { font-family: "Exo 2", sans-serif; font-style: italic; font-weight: 500; font-size: 34px; color: var(--orange); letter-spacing: 1px; }

  .service-list { position: absolute; top: 802px; list-style: none; color: var(--white); font-size: 29px; line-height: 37.8px; text-shadow: 0 2px 3px rgba(0,0,0,0.7); }
  .service-list li::before { content: "» "; }
  .service-list.left { left: 50px; }
  .service-list.right { left: 444px; }

  .hazard-band { position: absolute; left: 0; top: 1090px; width: 892px; height: 23px; }

  .cta-bar { position: absolute; left: 0; top: 1113px; width: 892px; height: 87px; display: flex; }
  .cta-message { width: 543px; background: var(--orange); display: flex; align-items: center; padding-left: 28px; font-family: "Exo 2", sans-serif; font-style: italic; font-weight: 500; font-size: 27px; letter-spacing: 2px; color: var(--ink); text-transform: uppercase; }
  .cta-phone { flex: 1; background: var(--charcoal); display: flex; align-items: center; padding-left: 22px; gap: 10px; color: var(--white); font-weight: 700; font-size: 44px; }
  .phone-arrow { width: 50px; height: 60px; }
</style>
</head>
<body>
<div class="flyer">
  <div class="headline-bar"><span class="headline">If You Want It Done Fast!!!</span></div>

  <div class="hero-photo" role="img" aria-label="Photo of a tracked skid steer lifting a bucket of dirt on a cleared site with trees behind"></div>

  <svg class="hero-fade" viewBox="0 0 892 420" aria-hidden="true">
    <defs>
      <linearGradient id="wedge" x1="0" y1="0" x2="0" y2="1">
        <stop offset="0" stop-color="#272421" stop-opacity="0.6"/>
        <stop offset="0.35" stop-color="#272421"/>
      </linearGradient>
    </defs>
    <polygon points="0,20 430,187 892,110 892,420 0,420" fill="url(#wedge)"/>
  </svg>

  <svg class="badge" viewBox="0 0 178 164" aria-hidden="true">
    <path d="M89 4 Q96 0 102 8 L172 138 Q176 150 164 152 L14 156 Q2 156 6 144 L78 10 Q82 4 89 4 Z" fill="var(--orange)"/>
    <path d="M150 130 L170 140 L160 158 Z" fill="#f3e2d3"/>
  </svg>
  <div class="badge-text">
    <span class="small">All</span>
    <span class="small">aspects</span>
    <span class="small">of Korvex</span>
    <span class="large">WORK!</span>
  </div>

  <div class="brand">
    <span class="brand-name">Marlo Dune</span>
    <span class="brand-sub">Earthworks</span>
  </div>

  <div class="soil-photo" role="img" aria-label="Close-up photo of freshly turned brown soil"></div>

  <div class="services-head">
    <svg class="services-icon" viewBox="0 0 52 52" aria-hidden="true">
      <circle cx="26" cy="26" r="26" fill="var(--orange)"/>
      <polyline points="20,15 32,26 20,37" fill="none" stroke="#fff" stroke-width="3"/>
    </svg>
    <span class="services-title">SERVICES:</span>
  </div>

  <ul class="service-list left">
    <li>Site Cleans</li>
    <li>Pavings Preps</li>
    <li>House Pads</li>
    <li>Final Trim Of Yard Demos</li>
    <li>Landscaping</li>
    <li>Pool Digs</li>
    <li>Earth Moving</li>
  </ul>
  <ul class="service-list right">
    <li>Rubbish Removal</li>
    <li>House And Shed Pads</li>
    <li>Paving Prep Concrete Removal</li>
    <li>Lawn Removal</li>
    <li>Clearing Limestone Driveways</li>
    <li>Limestone Block Lifting</li>
    <li>Levelling</li>
  </ul>

  <svg class="hazard-band" viewBox="0 0 892 23" aria-hidden="true">
    <defs>
      <pattern id="stripes" width="48" height="23" patternUnits="userSpaceOnUse">
        <polygon points="10,23 22,0 46,0 34,23" fill="var(--orange)"/>
      </pattern>
    </defs>
    <rect width="892" height="23" fill="var(--ink)"/>
    <rect width="892" height="23" fill="url(#stripes)"/>
  </svg>

  <div class="cta-bar">
    <div class="cta-message">Call today for a free quote!</div>
    <div class="cta-phone">
      <svg class="phone-arrow" viewBox="0 0 50 60" aria-hidden="true">
        <path d="M12 40 L12 26 Q12 12 26 12 L32 12 L32 4 L46 18 L32 32 L32 24 L26 24 Q24 24 24 26 L24 40 Z" fill="#fff" transform="rotate(90 25 30)"/>
      </svg>
      <span class="phone-number">0491 570 156</span>
    </div>
  </div>
</div>
</body>
</html>
```